Web re-design project www.varvikworks.com

We need a corporate website for a startup company called Varvik Works. The company offers web-based worksite management system for big construction companies. In short, replacing annoying papers with iPads.
We need the site main page to provide basic overview of the company and then inner page layout for displaying news and detailed information about products.
Currently we have a site up at:
http://www.varvikworks.com/en/main
but as you can see the graphic design is a bit lacking in quality(implemented by a tech guy :)
We need you to pimp that web site design up!
There is possibility for more freelance work in the future related to our web products, slide show designs and printed marketing materials.
Our main product is PELMO. You can find a short presentation about what it does here:
http://www.varvikworks.com/en/pelmo
Here you can find packages of images and screenshots related to our company:
https://files.stashbin.example/u/7720419/varvik_images.zip
https://files.stashbin.example/u/7720419/varvikworks%20images2.zip
Product logo svg can be found here:
https://files.stashbin.example/u/7720419/PELMO-logo.svg
Your are not forced to use those images, but hopefully there will be something that is useful.
Hope to hear from you guys soon!
Cheers,
Aarni
Update:
We will be using PELMO logo as the company brand. I don't like our current Varvik Works company logo, so that doesn't need to be included in the site design.
Update 2:
I like website designs that are "light", elegant and pretty simplistic. One example is our product login page (screenshot included in files).
Update 3:
Sites from the same industry / type of products:
http://www.rakomesta.fi/
http://www.brellinsurvey.com/products/software/network-applications/gradelane-3d
http://www.quostar.com/construction/heavy-civil/software-solutions/Linked-Crewfield.aspx?dtID=overview&
Target Market(s)
Target audience for the website is companies in the construction sector, and possibly corporate investors
Industry/Entity Type
Graphic Design
Look and feel

```html
<!DOCTYPE html>
<html lang="en">
<head>
<meta charset="utf-8">
<title>PELMO – Varvik Works</title>
<link rel="stylesheet" href="https://fonts.googleapis.com/css2?family=Montserrat:ital,wght@0,400;0,700;1,400&family=Source+Sans+3:wght@400;600;700&display=swap">
<style>
  :root {
    --bg-red: #a81b1b;
    --bg-orange: #c9491f;
    --white: #ffffff;
    --ink: #1a1a1a;
    --text: #4a4a4a;
    --muted: #5c5c5c;
    --rule: #cfcfcf;
    --hero-blue: rgba(24, 88, 140, 0.92);
    --card-blue: #2f8ace;
    --date-red: #b3262a;
    --icon-blue: #5c8fc4;
  }
  * { margin: 0; padding: 0; box-sizing: border-box; }
  html, body { width: 1200px; height: 1039px; overflow: hidden; }
  body {
    position: relative;
    background: linear-gradient(90deg, var(--bg-red) 0%, #b02420 55%, var(--bg-orange) 100%);
    font-family: "Source Sans 3", Arial, sans-serif;
    color: var(--text);
  }
  .page {
    position: absolute; left: 155px; top: 30px;
    width: 891px; height: 926px;
    background: var(--white);
  }
  .brand {
    position: absolute; left: 16px; top: 46px;
    display: flex; align-items: center; gap: 12px;
  }
  .brand-dot { width: 34px; height: 34px; border-radius: 50%; background: var(--ink); }
  .brand-name {
    font-family: "Source Sans 3", Arial, sans-serif;
    font-size: 40px; font-weight: 400; color: var(--ink); letter-spacing: 0.5px; line-height: 1;
  }
  .main-nav { position: absolute; top: 24px; left: 607px; display: flex; }
  .main-nav a {
    display: block; height: 42px; padding: 24px 0 0 8px;
    border-left: 1px solid var(--rule);
    font-size: 12px; color: var(--muted); text-decoration: none; text-transform: uppercase;
  }
  .main-nav a:nth-child(1) { width: 64px; }
  .main-nav a:nth-child(2) { width: 86px; }
  .main-nav a:nth-child(3) { width: 62px; }
  .main-nav a:nth-child(4) { width: 72px; }

  .hero { position: absolute; left: 0; top: 83px; width: 891px; height: 403px; overflow: hidden; }
  .hero-photo {
    position: absolute; inset: 0;
    background:
      linear-gradient(180deg, #c9d9a8 0%, #6f8f45 40%, #5d6a3a 70%, #6a5d3e 100%);
  }
  .hero-photo::after {
    content: ""; position: absolute; left: 380px; top: 0; width: 420px; height: 403px;
    background: radial-gradient(ellipse at 40% 45%, rgba(230,180,30,0.75), rgba(230,180,30,0) 65%);
  }
  .hero-panel {
    position: absolute; left: 0; top: 0; width: 327px; height: 403px;
    background: var(--hero-blue);
  }
  .hero-title {
    position: absolute; left: 23px; top: 26px; width: 300px;
    font-family: "Montserrat", Arial, sans-serif; font-weight: 700;
    font-size: 22.5px; line-height: 29px; color: var(--white);
  }
  .contact-card {
    position: absolute; left: 26px; top: 205px; width: 275px; height: 164px;
    background: var(--card-blue); border-radius: 2px;
    padding: 12px 0 0 19px;
    font-family: "Montserrat", Arial, sans-serif; font-style: italic;
    font-size: 15.5px; line-height: 25px; color: var(--white);
  }
  .contact-card p + p { margin-top: 24px; }

  .news-column { position: absolute; left: 18px; top: 512px; width: 361px; }
  .section-title {
    font-size: 16px; font-weight: 600; color: var(--ink); text-transform: uppercase; letter-spacing: -0.2px;
  }
  .news-column .section-title { padding-bottom: 10px; border-bottom: 1px solid var(--rule); }
  .news-item { position: relative; height: 166px; border-bottom: 1px solid var(--rule); }
  .news-date {
    position: absolute; left: 1px; top: 16px; width: 46px; height: 45px;
    background: linear-gradient(#fafafa, #e6e6e6); border: 1px solid #d8d8d8; border-radius: 3px;
    text-align: center; color: var(--date-red);
  }
  .news-date .month { display: block; font-size: 10px; font-weight: 600; margin-top: 4px; text-transform: uppercase; }
  .news-date .day { display: block; font-size: 23px; font-weight: 700; line-height: 22px; }
  .news-body { position: absolute; left: 63px; top: 21px; width: 285px; }
  .news-body h3 { font-size: 17px; font-weight: 700; color: var(--ink); margin-bottom: 8px; }
  .news-body p { font-size: 14.5px; line-height: 23px; color: var(--text); }
  .connect { margin-top: 38px; }
  .social-links { display: flex; gap: 5px; margin-top: 12px; }
  .social-links span { width: 21px; height: 21px; border-radius: 4px; background: var(--icon-blue); }

  .column-divider { position: absolute; left: 379px; top: 512px; width: 1px; height: 372px; background: var(--rule); }
  .product-column { position: absolute; left: 411px; top: 512px; width: 460px; }
  .product-visual {
    position: absolute; left: 58px; top: 64px; width: 290px; height: 276px;
    background: radial-gradient(ellipse at 60% 30%, #f2f2f2 0%, #e4e4e4 55%, #d6d6d6 100%);
    border-radius: 12px;
  }

  .site-footer { position: absolute; left: 0; top: 972px; width: 1200px; text-align: center; color: var(--white); }
  .footer-nav { font-size: 11.5px; word-spacing: 2px; }
  .footer-nav a { color: var(--white); text-decoration: none; }
  .footer-nav .sep { margin: 0 14px; }
  .copyright { font-size: 11px; margin-top: 11px; }
</style>
</head>
<body>
  <div class="page">
    <header>
      <div class="brand"><span class="brand-dot"></span><span class="brand-name">PELMO</span></div>
      <nav class="main-nav">
        <a href="#">Home</a><a href="#">Products</a><a href="#">News</a><a href="#">Contact</a>
      </nav>
    </header>

    <section class="hero">
      <div class="hero-photo" role="img" aria-label="Photo of a yellow excavator on a green roadwork site with workers in high-visibility vests"></div>
      <div class="hero-panel">
        <h1 class="hero-title">PELMO is a cloud-based service for road construction projects and it's going full steam!</h1>
        <address class="contact-card">
          <p>Varvik Works<br>Valssikatu 9, 00510 Helsinki</p>
          <p>Aarni Lehtola<br>+358 50 555 0142<br>aarni.lehtola@varvikworks.com</p>
        </address>
      </div>
    </section>

    <section class="news-column">
      <h2 class="section-title">Latest News</h2>
      <article class="news-item">
        <div class="news-date"><span class="month">Oct</span><span class="day">25</span></div>
        <div class="news-body">
          <h3>Welcome to our new website!</h3>
          <p>Varvik Works new website has been launched. From these pages you can find information about PELMO cloud-based road construction service and other products from Varvik Works.</p>
        </div>
      </article>
      <div class="connect">
        <h2 class="section-title">Connect with us</h2>
        <div class="social-links"><span></span><span></span><span></span><span></span></div>
      </div>
    </section>

    <div class="column-divider"></div>

    <section class="product-column">
      <h2 class="section-title">PELMO - Web based worksite data management service</h2>
      <div class="product-visual" role="img" aria-label="Illustration of a person at a computer thinking about schedules, road profiles and excavators"></div>
    </section>
  </div>

  <footer class="site-footer">
    <nav class="footer-nav">
      <a href="#">Home</a><span class="sep">-</span><a href="#">Products</a><span class="sep">-</span><a href="#">News</a><span class="sep">-</span><a href="#">Contact</a>
    </nav>
    <p class="copyright">Copyright © pelmo 2012. All rights reserved.</p>
  </footer>
</body>
</html>
```